Appealing productlabel for jar with toffees

I run a small import company within confectionary (candy, chocolate, toffees and so on). We are planning launching a series of bulk product - and would like to start up with this article enclosed.<br/>Packaging: Transparent plastic Jar with black lid. Height 22 cm, diameter 15 cm.<br/>I was thinking about a label with the dimensions 10,5 x 14,8 cm. since a have a label sheet in this format (I will probably end up getting it printed at a professional printing company)<br/>Unique Selling Points: Great Toffees with great taste. The toffees do NOT stick to your teeth, 1000 gram, hygienically wrapped.<br/>Brand Name ROVA<br/><br/>Buyers/ Clients: Office Supplies

Target Market(s)

Adult professional purchasers within the segmment: Office Supply, Food Service

Font styles to use
Serif

Requirements
Must have
• Appealing, catchy, attractive design
Nice to have
• Surprise me :-)
Should not have
• A traditional candy design which is appealing to kids - the clients will be grown-ups

```html
<!DOCTYPE html>
<html lang="da">
<head>
<meta charset="utf-8">
<title>Luna Candy – Karameller med Havsalt – label variants</title>
<link href="https://fonts.googleapis.com/css2?family=Alfa+Slab+One&family=Kaushan+Script&family=Montserrat:ital,wght@0,400;0,700;0,800;1,400&display=swap" rel="stylesheet">
<style>
  :root {
    --page: #ffffff;
    --pattern: #c0def2;
    --frame-blue: #12a8e6;
    --frame-green: #b7dcb0;
    --title-blue: #8ccff5;
    --ink: #1b1b1b;
    --muted: #6d6d6d;
    --light: #ffffff;
    --dark-panel: #000000;
    --dark-glass: rgba(28, 34, 40, 0.9);
    --white-glass: rgba(255, 255, 255, 0.86);
  }
  * { margin: 0; padding: 0; box-sizing: border-box; }
  html, body { width: 1200px; height: 915px; overflow: hidden; background: var(--page); }
  .sheet { position: relative; width: 1200px; height: 915px; }
  .variant-number {
    position: absolute; font-family: "Montserrat", sans-serif; font-weight: 700;
    font-size: 22px; color: var(--ink); line-height: 1;
  }
  .label {
    position: absolute; width: 534px; height: 379px; background: var(--pattern);
    box-shadow: 0 0 22px rgba(0,0,0,0.08);
  }
  .label svg { display: block; width: 100%; height: 100%; }
  .pattern-area { fill: var(--pattern); }
  .frame-outer { fill: none; stroke: var(--frame-blue); stroke-width: 7; }
  .frame-echo { fill: none; stroke: var(--frame-green); stroke-width: 6; }
  .frame-inner { stroke: var(--frame-blue); stroke-width: 4; }
  .brand { font-family: "Montserrat", sans-serif; font-weight: 800; font-size: 29px; text-anchor: middle; }
  .tagline { font-family: "Montserrat", sans-serif; font-style: italic; font-size: 20px; letter-spacing: 1px; text-anchor: middle; }
  .product { font-family: "Alfa Slab One", serif; font-size: 47px; letter-spacing: 2px; fill: var(--title-blue); text-anchor: middle; }
  .joiner { font-family: "Kaushan Script", cursive; font-size: 50px; fill: var(--title-blue); text-anchor: middle; }
  .rule { stroke-width: 4; }
  .claims { font-family: "Montserrat", sans-serif; font-size: 15px; text-anchor: middle; }
  .light .inner-fill { fill: var(--light); }
  .light .glass-fill { fill: var(--white-glass); }
  .light .brand { fill: var(--ink); }
  .light .tagline { fill: var(--muted); }
  .light .rule { stroke: var(--ink); }
  .light .claims { fill: var(--ink); }
  .dark .inner-fill { fill: var(--dark-panel); }
  .dark .glass-fill { fill: var(--dark-glass); }
  .dark .brand, .dark .tagline, .dark .claims { fill: var(--light); }
  .dark .rule { stroke: var(--light); }
</style>
</head>
<body>
<main class="sheet">
  <span class="variant-number" style="left:41px;top:26px">1</span>
  <span class="variant-number" style="left:1129px;top:26px">2</span>
  <span class="variant-number" style="left:42px;top:868px">3</span>
  <span class="variant-number" style="left:1129px;top:868px">4</span>

  <!-- Variant 1: solid white -->
  <section class="label light" style="left:56px;top:59px">
    <svg viewBox="0 0 980 695" preserveAspectRatio="none">
      <rect class="pattern-area" width="980" height="695" role="img" aria-label="Pastel pattern of scattered sweets, lollipops and candy canes in soft blue, green, pink and grey"/>
      <polygon class="frame-echo" points="487,98 710,225 710,485 487,613 262,485 262,225"/>
      <polygon class="frame-outer" points="475,90 698,217 698,477 475,605 250,477 250,217"/>
      <polygon class="frame-inner inner-fill" points="475,114 676,229 676,467 475,582 271,467 271,229"/>
      <text class="brand" x="472" y="212">LUNA CANDY</text>
      <text class="tagline" x="472" y="244">Keep it Sweet &amp; Simple</text>
      <text class="product" x="477" y="316">KARAMELLER</text>
      <line class="rule" x1="314" y1="352" x2="404" y2="352"/>
      <text class="joiner" x="478" y="372">med</text>
      <line class="rule" x1="551" y1="352" x2="641" y2="352"/>
      <text class="product" x="477" y="432">HAVSALT</text>
      <text class="claims" x="481" y="464">Cool karameller der</text>
      <text class="claims" x="481" y="487">Ikke klistrer I tænderne</text>
      <text class="claims" x="481" y="510">Pjattet gode og</text>
      <text class="claims" x="481" y="533">Imponerende</text>
    </svg>
  </section>

  <!-- Variant 2: solid black -->
  <section class="label dark" style="left:608px;top:59px">
    <svg viewBox="0 0 980 695" preserveAspectRatio="none">
      <rect class="pattern-area" width="980" height="695" role="img" aria-label="Pastel pattern of scattered sweets, lollipops and candy canes in soft blue, green, pink and grey"/>
      <polygon class="frame-echo" points="487,98 710,225 710,485 487,613 262,485 262,225"/>
      <polygon class="frame-outer" points="475,90 698,217 698,477 475,605 250,477 250,217"/>
      <polygon class="frame-inner inner-fill" points="475,114 676,229 676,467 475,582 271,467 271,229"/>
      <text class="brand" x="472" y="212">LUNA CANDY</text>
      <text class="tagline" x="472" y="244">Keep it Sweet &amp; Simple</text>
      <text class="product" x="477" y="316">KARAMELLER</text>
      <line class="rule" x1="314" y1="352" x2="404" y2="352"/>
      <text class="joiner" x="478" y="372">med</text>
      <line class="rule" x1="551" y1="352" x2="641" y2="352"/>
      <text class="product" x="477" y="432">HAVSALT</text>
      <text class="claims" x="481" y="464">Cool karameller der</text>
      <text class="claims" x="481" y="487">Ikke klistrer I tænderne</text>
      <text class="claims" x="481" y="510">Pjattet gode og</text>
      <text class="claims" x="481" y="533">Imponerende</text>
    </svg>
  </section>

  <!-- Variant 3: translucent white -->
  <section class="label light" style="left:56px;top:468px">
    <svg viewBox="0 0 980 695" preserveAspectRatio="none">
      <rect class="pattern-area" width="980" height="695" role="img" aria-label="Pastel pattern of scattered sweets, lollipops and candy canes in soft blue, green, pink and grey"/>
      <polygon class="frame-echo" points="487,98 710,225 710,485 487,613 262,485 262,225"/>
      <polygon class="frame-outer" points="475,90 698,217 698,477 475,605 250,477 250,217"/>
      <polygon class="frame-inner glass-fill" points="475,114 676,229 676,467 475,582 271,467 271,229"/>
      <text class="brand" x="472" y="212">LUNA CANDY</text>
      <text class="tagline" x="472" y="244">Keep it Sweet &amp; Simple</text>
      <text class="product" x="477" y="316">KARAMELLER</text>
      <line class="rule" x1="314" y1="352" x2="404" y2="352"/>
      <text class="joiner" x="478" y="372">med</text>
      <line class="rule" x1="551" y1="352" x2="641" y2="352"/>
      <text class="product" x="477" y="432">HAVSALT</text>
      <text class="claims" x="481" y="464">Cool karameller der</text>
      <text class="claims" x="481" y="487">Ikke klistrer I tænderne</text>
      <text class="claims" x="481" y="510">Pjattet gode og</text>
      <text class="claims" x="481" y="533">Imponerende</text>
    </svg>
  </section>

  <!-- Variant 4: translucent dark -->
  <section class="label dark" style="left:608px;top:468px">
    <svg viewBox="0 0 980 695" preserveAspectRatio="none">
      <rect class="pattern-area" width="980" height="695" role="img" aria-label="Pastel pattern of scattered sweets, lollipops and candy canes in soft blue, green, pink and grey"/>
      <polygon class="frame-echo" points="487,98 710,225 710,485 487,613 262,485 262,225"/>
      <polygon class="frame-outer" points="475,90 698,217 698,477 475,605 250,477 250,217"/>
      <polygon class="frame-inner glass-fill" points="475,114 676,229 676,467 475,582 271,467 271,229"/>
      <text class="brand" x="472" y="212">LUNA CANDY</text>
      <text class="tagline" x="472" y="244">Keep it Sweet &amp; Simple</text>
      <text class="product" x="477" y="316">KARAMELLER</text>
      <line class="rule" x1="314" y1="352" x2="404" y2="352"/>
      <text class="joiner" x="478" y="372">med</text>
      <line class="rule" x1="551" y1="352" x2="641" y2="352"/>
      <text class="product" x="477" y="432">HAVSALT</text>
      <text class="claims" x="481" y="464">Cool karameller der</text>
      <text class="claims" x="481" y="487">Ikke klistrer I tænderne</text>
      <text class="claims" x="481" y="510">Pjattet gode og</text>
      <text class="claims" x="481" y="533">Imponerende</text>
    </svg>
  </section>
</main>
</body>
</html>
```